Create a business promotion flyer to leave in customer mailboxes. We are a bulk petroleum supplier, servicing any industry that requires diesel. Base in griffith NSW, servicing griffith area and surrounds.

Business Name - Terra Petro
Fuel@terrapetro-example.com.au
Marco - 0400 000 001 mtorrisi@terrapetro-example.com.au
Liam - 0400 000 002 lharcourt@terrapetro-example.com.au
Peter - 0400 000 003 pwinslow@terrapetro-example.com.au
Office 02 5550 0100

Bulk Fuel deliveries.
Oils & lubricants
Local Family owned business

```html
<!DOCTYPE html>
<html lang="en">
<head>
<meta charset="utf-8">
<title>Terra Petro – Flyer</title>
<link rel="stylesheet" href="https://fonts.googleapis.com/css2?family=Poppins:wght@400;600;700;800&family=Yellowtail&display=swap">
<style>
  :root{
    --red:#e8262a;
    --red-deep:#c8161b;
    --charcoal:#3a3a3c;
    --ink:#2b2b2d;
    --paper:#ffffff;
    --stage:#ececec;
    --muted:#444446;
  }
  *{box-sizing:border-box;margin:0;padding:0}
  html,body{width:1200px;height:735px;overflow:hidden}
  body{background:var(--stage);font-family:"Poppins",sans-serif;color:var(--ink)}
  .flyer{position:absolute;left:352px;top:17px;width:495px;height:700px;background:var(--paper);overflow:hidden;box-shadow:0 2px 10px rgba(0,0,0,.12)}
  .abs{position:absolute}
  .hero{left:0;top:0;width:495px;height:420px}
  .brand{left:18px;top:58px;font-weight:600;font-size:38px;line-height:1;color:var(--red);letter-spacing:-.5px}
  .headline-band{left:0;top:333px;width:152px;height:31px;background:var(--red)}
  .headline-1{left:19px;top:332px;font-weight:800;font-size:27px;line-height:33px;color:var(--paper);letter-spacing:.3px}
  .headline-2{left:19px;top:366px;font-weight:800;font-size:28px;line-height:32px;color:var(--charcoal);letter-spacing:.2px}
  .headline-3{left:19px;top:398px;font-weight:700;font-size:13.5px;line-height:16px;color:var(--muted)}
  .intro{left:19px;top:430px;width:210px;font-size:10.2px;line-height:12px;color:var(--ink)}
  .family{left:19px;top:506px}
  .family .script{font-family:"Yellowtail",cursive;font-size:24px;line-height:22px;color:var(--red)}
  .family .label{font-weight:800;font-size:10.5px;line-height:11px;color:var(--charcoal);padding-left:4px}
  .region{left:143px;top:535px;width:66px;height:60px;background:var(--red);border-radius:10px 16px 6px 14px}
  .region-pin{left:158px;top:517px}
  .region-text{left:150px;top:558px;font-weight:700;font-size:11px;line-height:12px;color:var(--paper)}
  .contact-band{left:0;top:583px;width:154px;height:22px;background:var(--charcoal);border-radius:0 5px 5px 0;color:var(--paper);font-weight:700;font-size:10.5px;line-height:22px;padding-left:19px}
  .contacts{left:19px;top:613px;display:flex}
  .contact{font-size:10px;line-height:10px;padding-right:8px;margin-right:8px;border-right:1px solid #999}
  .contact:last-child{border-right:0}
  .contact .name{display:block;font-weight:700;color:var(--red);text-transform:uppercase}
  .contact .phone{display:block;color:var(--ink)}
  .info{left:19px;font-size:10.2px;line-height:10.5px;display:flex;gap:5px;color:var(--ink)}
  .info svg{flex:none;margin-top:1px}
  .services{left:293px;top:420px;width:202px;height:272px;background:var(--red)}
  .services-head{left:293px;top:420px;width:202px;height:38px;background:var(--charcoal);color:var(--paper);font-weight:800;font-size:27px;line-height:38px;padding-left:23px}
  .service-icon{width:52px;height:52px;border-radius:50%;background:var(--charcoal);border:2px solid var(--paper);display:flex;align-items:center;justify-content:center}
  .service{left:317px;width:170px;color:var(--paper)}
  .service h3{font-weight:700;font-size:13.5px;line-height:15px;margin-bottom:2px}
  .service p{font-size:10px;line-height:12px}
  .foot-red{left:0;top:692px;width:35px;height:8px;background:var(--red)}
  .foot-dark{left:35px;top:692px;width:420px;height:8px;background:var(--charcoal)}
</style>
</head>
<body>
<main class="flyer">
  <svg class="abs hero" viewBox="0 0 495 420" width="495" height="420">
    <defs>
      <linearGradient id="liquidTone" x1="0" y1="0" x2="1" y2="1">
        <stop offset="0" stop-color="#f2541c"/><stop offset=".5" stop-color="#d8230f"/><stop offset="1" stop-color="#9c1208"/>
      </linearGradient>
      <linearGradient id="yardTone" x1="0" y1="0" x2="0" y2="1">
        <stop offset="0" stop-color="#8e969e"/><stop offset=".35" stop-color="#b8bcc0"/><stop offset=".55" stop-color="#e7e7e5"/><stop offset=".75" stop-color="#b3aea8"/><stop offset="1" stop-color="#a9a49e"/>
      </linearGradient>
      <radialGradient id="splashTone" cx=".5" cy=".5" r=".5">
        <stop offset="0" stop-color="#e6b73a" stop-opacity=".95"/><stop offset=".6" stop-color="#c99a1f" stop-opacity=".6"/><stop offset="1" stop-color="#c99a1f" stop-opacity="0"/>
      </radialGradient>
    </defs>
    <polygon points="255,0 370,0 320,48" fill="var(--charcoal)"/>
    <polygon role="img" aria-label="Close-up of glowing red-orange fuel liquid" points="370,0 495,0 495,240 240,150 320,48" fill="url(#liquidTone)"/>
    <polygon role="img" aria-label="Photo of a white road-train fuel tanker parked in front of a steel depot shed" points="0,155 240,114 495,150 495,420 0,420" fill="url(#yardTone)"/>
    <ellipse role="img" aria-label="Splash of golden lubricating oil" cx="430" cy="365" rx="75" ry="70" fill="url(#splashTone)"/>
  </svg>

  <div class="abs brand">Terra Petro</div>

  <div class="abs headline-band"></div>
  <h1 class="abs headline-1">FUELING</h1>
  <div class="abs headline-2">LOCAL INDUSTRY</div>
  <div class="abs headline-3">IN GRIFFITH &amp; SURROUNDS</div>

  <p class="abs intro">Terra Petro is a local, family owned business proudly supplying high quality fuel and lubricants to businesses, farms and industry across the Griffith region.</p>

  <div class="abs family">
    <div class="script">Local</div>
    <div class="label">FAMILY OWNED<br>BUSINESS</div>
  </div>

  <div class="abs region" role="img" aria-label="Map outline of the Griffith NSW region"></div>
  <svg class="abs region-pin" width="18" height="26" viewBox="0 0 18 26"><path d="M9 1a8 8 0 0 0-8 8c0 6 8 16 8 16s8-10 8-16a8 8 0 0 0-8-8z" fill="var(--red)" stroke="#fff" stroke-width="1.5"/><circle cx="9" cy="9" r="3" fill="#fff"/></svg>
  <div class="abs region-text">Griffith<br>NSW</div>

  <div class="abs contact-band">GET IN TOUCH TODAY</div>
  <div class="abs contacts">
    <div class="contact"><span class="name">Marco</span><span class="phone">0400 000 001</span></div>
    <div class="contact"><span class="name">Liam</span><span class="phone">0400 000 002</span></div>
    <div class="contact"><span class="name">Peter</span><span class="phone">0400 000 003</span></div>
  </div>
  <div class="abs info" style="top:645px">
    <svg width="11" height="8" viewBox="0 0 11 8"><rect width="11" height="8" rx="1" fill="var(--red)"/><path d="M0.5 .8 5.5 4.6 10.5 .8" stroke="#fff" stroke-width="1" fill="none"/></svg>
    <span>Fuel@terrapetro-example.com.au</span>
  </div>
  <div class="abs info" style="top:660px">
    <svg width="11" height="13" viewBox="0 0 11 13"><path d="M5.5 .5a5 5 0 0 0-5 5c0 3.6 5 7 5 7s5-3.4 5-7a5 5 0 0 0-5-5z" fill="var(--red)"/><circle cx="5.5" cy="5.3" r="1.8" fill="#fff"/></svg>
    <span>Based in Griffith NSW, servicing Griffith<br>area and surrounds.</span>
  </div>

  <section class="abs services"></section>
  <h2 class="abs services-head">SERVICES</h2>

  <div class="abs service-icon" style="left:255px;top:481px">
    <svg width="30" height="20" viewBox="0 0 30 20" fill="none" stroke="#fff" stroke-width="1.8"><rect x="1" y="3" width="17" height="9" rx="4.5"/><path d="M19 6h5l4 5v4H1v-3"/><circle cx="7" cy="16" r="2.2"/><circle cx="23" cy="16" r="2.2"/></svg>
  </div>
  <div class="abs service" style="top:490px"><h3>BULK FUEL DELIVERIES</h3><p>Reliable on-time delivery<br>of premium diesel to keep<br>your business moving.</p></div>

  <div class="abs service-icon" style="left:255px;top:553px">
    <svg width="28" height="24" viewBox="0 0 28 24" fill="#fff"><path d="M7 4s-6 7-6 11a6 6 0 0 0 12 0C13 11 7 4 7 4z"/><rect x="14" y="3" width="13" height="19" rx="3" fill="none" stroke="#fff" stroke-width="2"/><path d="M14 9h13M14 16h13" stroke="#fff" stroke-width="2"/></svg>
  </div>
  <div class="abs service" style="top:560px"><h3>OILS &amp; LUBRICANTS</h3><p>High quality products to<br>keep your equipment<br>running at its best.</p></div>

  <div class="abs service-icon" style="left:255px;top:623px">
    <svg width="22" height="26" viewBox="0 0 22 26" fill="none" stroke="#fff" stroke-width="2"><path d="M3 6h10l6 5v13H3z"/><path d="M6 6V2h5v4"/><path d="M11 12s-3 4-3 6a3 3 0 0 0 6 0c0-2-3-6-3-6z" fill="#fff" stroke="none"/></svg>
  </div>
  <div class="abs service" style="top:630px"><h3>PETROL DELIVERIES</h3><p>Convenient petrol<br>deliveries for all your<br>business needs.</p></div>

  <div class="abs foot-red"></div>
  <div class="abs foot-dark"></div>
</main>
</body>
</html>
```